Logo für Trockenbauarbeiten aller Art, Spachtelarbeiten und Verputzarbeiten
Zielgruppe
Gegenstand des Unternehmens ist Trockenbauarbeiten aller Art, Spachtelarbeiten und Verputzarbeiten.
Unsere Zielgruppe sind Menschen ab 30 Jahren aufwärts, wir interessieren uns für den einzelnen Hausbesitzer oder Eigentumswohnungbesitzer. Wir benötigen einen hohen Wiedererkennungseffekt.
Wir benötigen Designvorlagen für eine Facebook Seite, Instagram und werden über diese beiden Plattformen auch Werbung schalten, daher benötigen wir dafür auch die verschiedenen Designvorlagen, um verschiedenen Werbekampangen zu erstellen.
Name des Unternehmens: 'WAND-PLAN KOLLHAGEN GmbH'
Aufgabenstellung
Wichtig ist bei den verschiedenen Designs, dass wir Leads bzw. Kundenaufträge sammeln können. Wir müssen herausstechen aus der Masse an Handwerkern. Wir sind die absoluten Spezialisten in unserem Gebiet. Des Weiteren werden wir aus den Materialen diverse Kampagnen erstellen die das komplette Jahr 2022 durchlaufen werden. Vorzugsweise werden wir hierfür die Plattfirm Facebook verwenden, aber auch andere Kanäle.
WICHTIG: Das Logo mit dem roten Haus ist unser original Logo!

```html
<!DOCTYPE html>
<html lang="de">
<head>
<meta charset="utf-8">
<title>Wand-Plan Kollhagen – Social Post</title>
<link rel="stylesheet" href="https://fonts.googleapis.com/css2?family=Montserrat:wght@700;800&family=Open+Sans:wght@400;700&display=swap">
<style>
  :root {
    --surround: #262427;
    --charcoal: #353230;
    --brand-red: #ff0000;
    --white: #ffffff;
    --ink: #1f1d1c;
    --photo-warm: #6b4f36;
    --photo-mid: #a8998a;
    --photo-light: #e6e3df;
  }
  * { margin: 0; padding: 0; box-sizing: border-box; }
  html, body { width: 1200px; height: 1200px; overflow: hidden; background: var(--surround); }
  .post {
    position: absolute; left: 104px; top: 104px; width: 992px; height: 992px;
    background: var(--white); overflow: hidden;
  }
  .post__photo {
    position: absolute; left: 0; top: 0; width: 992px; height: 600px;
    background: linear-gradient(90deg, var(--photo-warm) 0%, #7a5e44 38%, var(--photo-mid) 58%, var(--photo-light) 78%, #d9d6d1 100%);
  }
  .post__band {
    position: absolute; left: 0; top: 600px; width: 992px; height: 282px;
    background: var(--charcoal);
  }
  .brand {
    position: absolute; left: 120px; top: 110px;
    display: flex; align-items: center; gap: 14px;
    font-family: "Montserrat", sans-serif; font-weight: 800;
    font-size: 34px; line-height: 1.05; color: var(--white);
    letter-spacing: 0.5px;
  }
  .brand__mark { width: 22px; height: 22px; background: var(--brand-red); flex: none; }
  .headline-box {
    position: absolute; left: 37px; top: 457px; width: 447px; height: 535px;
    background: var(--brand-red); color: var(--white);
    padding: 42px 0 0 35px;
  }
  .headline-box__title {
    font-family: "Montserrat", sans-serif; font-weight: 800;
    font-size: 60px; line-height: 72px; letter-spacing: 0.3px;
  }
  .headline-box__rule { width: 217px; height: 4px; background: var(--white); margin: 30px 0 34px; }
  .headline-box__text {
    font-family: "Open Sans", sans-serif; font-size: 21.5px; line-height: 34px;
  }
  .about {
    position: absolute; left: 548px; top: 650px; width: 420px; color: var(--white);
  }
  .about__title {
    font-family: "Montserrat", sans-serif; font-weight: 800; font-size: 42px; line-height: 1.1;
    margin-bottom: 8px;
  }
  .about__text {
    font-family: "Open Sans", sans-serif; font-size: 19.5px; line-height: 30px;
  }
  .contact {
    position: absolute; left: 554px; top: 930px;
    display: flex; align-items: center; gap: 20px;
    font-family: "Open Sans", sans-serif; font-weight: 700; font-size: 38px; color: var(--ink);
  }
  .contact__icon { width: 50px; height: 50px; flex: none; }
</style>
</head>
<body>
  <main class="post">
    <div class="post__photo" role="img" aria-label="Foto: Handwerker auf einer Leiter montiert Gipskartonplatten an einer gedämmten Ständerwand"></div>
    <div class="post__band"></div>

    <div class="brand"><span class="brand__mark"></span><span>WAND-PLAN<br>KOLLHAGEN</span></div>

    <section class="headline-box">
      <h1 class="headline-box__title">Lorem<br>Ipsum dolor<br>sit amet</h1>
      <div class="headline-box__rule"></div>
      <p class="headline-box__text">Lorem ipsum dolor sit amet,<br>consectetur adipiscing elit, sed do<br>eiusmod tempor incididunt ut<br>labore et dolore magna<br>aliqua. Ut enim ad minim veniam,</p>
    </section>

    <section class="about">
      <h2 class="about__title">About us</h2>
      <p class="about__text">Lorem ipsum dolor sit amet, consectetur<br>adipiscing elit, sed do eiusmod tempor<br>incididunt ut labore et dolore magna<br>aliqua. Ut enim ad minim veniam,</p>
    </section>

    <div class="contact">
      <svg class="contact__icon" viewBox="0 0 50 50" aria-hidden="true">
        <path d="M10 6c2-1 4-1 5 1l4 8c1 2 0 3-1 4l-3 2c2 5 6 10 11 13l2-3c1-1 3-2 4-1l8 4c2 1 2 3 1 5l-2 4c-2 3-6 4-10 2C17 40 8 30 5 18c-1-4 1-9 5-12z" fill="var(--brand-red)"/>
        <path d="M28 12a11 11 0 0 1 10 10M29 6a17 17 0 0 1 15 15M30 0a22 22 0 0 1 20 20" fill="none" stroke="var(--brand-red)" stroke-width="2.5" stroke-linecap="round"/>
      </svg>
      <span>0170/4821936</span>
    </div>
  </main>
</body>
</html>
```